In-Design Template: Single-sided A3 Brochure

Hi In-Design Experts,

I am after an A3 template which is created using In-Design. It needs to be able to operate in CS3.

This template will be used as the basis for a brochure for a beautiful range of stationery. In order to help me with the layout of the brochure, I require a template to be created using "In-Design". The template that you will create will include Rectangle Frames that will allow me to easily insert my products.

As this template is hard to describe in words, I have attached a diagram of what I am actually after. This is an A3 brochure (created on a slightly bigger canvas). As you will see, the right side is an exact replica of the left side. In creating the brochure, think of beautiful shades of pinks - incorporating baby pinks and pastel pinks - elegant, classy and beautiful.

Further details provided below and in the attached files.

If you require any further information or have any questions, please let me know.

Looking forward to seeing your designs.

Target Market(s)

Women

Requirements
Must have
• Template must be created using "In-Design" and be able to operate in version CS3.
• Template information - In the supporting files, I have set out the following:
• - Size of template (Image A3 created on canvas size SRA3 (450 x 320mm) with crop marks
• - Location of all text areas
• - Location of the boxes for my products - Please use the "Rectangle Frame Tool" to allow me to insert products later on.
• Further Design Work - The template is the basis and I would then require your creativity for the following design work:
• - Text to be included at the top of each page - "Vitrel" using Edwarian Script (or similar font style. Please use the pink tones described above.
• - Image - I have attached an image that I would like to include in some way. I am thinking of placing this in the corners of the brochure - but opened to ideas. The image is a picture of scattered leaves. The picture I have attached is in shades of purple, however, I would require the leaves in shades of Pink. I am open to how you use these leaves in the template/brochure. You definitely do not need to use the exact leaves as displayed but something similar would be perfect.

```html
<!DOCTYPE html>
<html lang="en">
<head>
<meta charset="utf-8">
<title>Vitrel Stationery Brochure Template</title>
<link href="https://fonts.googleapis.com/css2?family=Great+Vibes&family=Pathway+Gothic+One&display=swap" rel="stylesheet">
<style>
  :root {
    --page: #ffffff;
    --blush-top: #f8d2e2;
    --blush-mid: #fdf2f7;
    --blush-low: #fffafc;
    --blush-bottom: #f9d6e5;
    --title-pink: #e4007f;
    --label-pink: #f4aacb;
    --frame-line: #a9a9a9;
    --ink: #2b2b2b;
    --flower: #f4a3b0;
    --flower-deep: #ee7aa5;
    --vine-soft: rgba(150, 196, 120, 0.30);
    --vine-fade: rgba(150, 196, 120, 0.10);
    --swirl-pink: rgba(238, 150, 185, 0.22);
  }
  html, body {
    margin: 0;
    padding: 0;
    width: 1200px;
    height: 880px;
    overflow: hidden;
    background: var(--page);
  }
  .sheet {
    position: relative;
    width: 1200px;
    height: 880px;
    background: var(--page);
  }
  .spread {
    position: absolute;
    left: 32px;
    top: 36px;
    width: 1135px;
    height: 808px;
    background: linear-gradient(180deg, var(--blush-top) 0%, var(--blush-mid) 30%, var(--blush-low) 50%, var(--blush-low) 75%, var(--blush-bottom) 100%);
    overflow: hidden;
  }
  .decor {
    position: absolute;
  }
  .corner-flower {
    top: 0;
    width: 208px;
    height: 200px;
    background: radial-gradient(circle at 55% 45%, var(--flower) 0%, rgba(244,163,176,0.55) 32%, rgba(248,210,226,0) 68%);
  }
  .corner-flower.left { left: 0; }
  .corner-flower.right { right: 0; }
  .vine {
    top: 0;
    width: 250px;
    height: 70px;
    background:
      radial-gradient(ellipse 50% 90% at 50% 0%, var(--vine-soft) 0%, var(--vine-fade) 45%, rgba(248,210,226,0) 100%),
      radial-gradient(ellipse 60% 100% at 50% 20%, var(--swirl-pink) 0%, rgba(248,210,226,0) 100%);
  }
  .vine.left { left: 215px; }
  .vine.right { left: 672px; }
  .center-bloom {
    left: 458px;
    top: 0;
    width: 222px;
    height: 190px;
    background: radial-gradient(circle at 50% 50%, #ffffff 0%, #ffffff 14%, var(--flower-deep) 28%, rgba(238,122,165,0.55) 50%, rgba(248,210,226,0) 75%);
  }
  .title {
    position: absolute;
    top: 100px;
    width: 300px;
    margin: 0;
    text-align: center;
    font-family: "Great Vibes", cursive;
    font-weight: 400;
    font-size: 74px;
    line-height: 1;
    color: var(--title-pink);
    text-shadow: 2px 3px 4px rgba(200, 80, 140, 0.35);
  }
  .title.left { left: 150px; }
  .title.right { left: 694px; }
  .note {
    position: absolute;
    width: 200px;
    margin: 0;
    text-align: center;
    font-family: "Pathway Gothic One", sans-serif;
    font-size: 12px;
    line-height: 14px;
    color: var(--ink);
  }
  .note.top.left { left: 192px; top: 181px; }
  .note.top.right { left: 751px; top: 179px; }
  .note.bottom.left { left: 188px; top: 773px; }
  .note.bottom.right { left: 756px; top: 773px; }
  .product-grid {
    position: absolute;
    top: 211px;
    display: grid;
    grid-template-columns: repeat(8, 53px);
    grid-auto-rows: 66px;
    column-gap: 13.7px;
    row-gap: 14px;
  }
  .product-grid.left { left: 28px; }
  .product-grid.right { left: 596px; }
  .product-frame {
    position: relative;
    box-sizing: border-box;
    border: 1px solid var(--frame-line);
    background: #ffffff;
  }
  .product-frame span {
    position: absolute;
    left: 0;
    right: 0;
    bottom: 0;
    height: 12px;
    background: var(--label-pink);
    font-family: "Pathway Gothic One", sans-serif;
    font-size: 10px;
    line-height: 12px;
    text-align: center;
    color: var(--ink);
  }
</style>
</head>
<body>
<div class="sheet">
  <div class="spread">
    <div class="decor corner-flower left" role="img" aria-label="Pink blossom with swirls and green leaves in the top-left corner"></div>
    <div class="decor vine left" role="img" aria-label="Green curling vine with leaves along the top edge"></div>
    <div class="decor center-bloom" role="img" aria-label="Central pink floral ornament with concentric circles and leaves"></div>
    <div class="decor vine right" role="img" aria-label="Green curling vine with leaves along the top edge"></div>
    <div class="decor corner-flower right" role="img" aria-label="Pink blossom with swirls and green leaves in the top-right corner"></div>

    <h1 class="title left">Vitrel</h1>
    <h1 class="title right">Vitrel</h1>

    <p class="note top left">Editable text box here</p>
    <p class="note top right">Editable text box here</p>

    <div class="product-grid left">
      <div class="product-frame"><span>TEXT</span></div><div class="product-frame"><span>TEXT</span></div><div class="product-frame"><span>TEXT</span></div><div class="product-frame"><span>TEXT</span></div><div class="product-frame"><span>TEXT</span></div><div class="product-frame"><span>TEXT</span></div><div class="product-frame"><span>TEXT</span></div><div class="product-frame"><span>TEXT</span></div>
      <div class="product-frame"><span>TEXT</span></div><div class="product-frame"><span>TEXT</span></div><div class="product-frame"><span>TEXT</span></div><div class="product-frame"><span>TEXT</span></div><div class="product-frame"><span>TEXT</span></div><div class="product-frame"><span>TEXT</span></div><div class="product-frame"><span>TEXT</span></div><div class="product-frame"><span>TEXT</span></div>
      <div class="product-frame"><span>TEXT</span></div><div class="product-frame"><span>TEXT</span></div><div class="product-frame"><span>TEXT</span></div><div class="product-frame"><span>TEXT</span></div><div class="product-frame"><span>TEXT</span></div><div class="product-frame"><span>TEXT</span></div><div class="product-frame"><span>TEXT</span></div><div class="product-frame"><span>TEXT</span></div>
      <div class="product-frame"><span>TEXT</span></div><div class="product-frame"><span>TEXT</span></div><div class="product-frame"><span>TEXT</span></div><div class="product-frame"><span>TEXT</span></div><div class="product-frame"><span>TEXT</span></div><div class="product-frame"><span>TEXT</span></div><div class="product-frame"><span>TEXT</span></div><div class="product-frame"><span>TEXT</span></div>
      <div class="product-frame"><span>TEXT</span></div><div class="product-frame"><span>TEXT</span></div><div class="product-frame"><span>TEXT</span></div><div class="product-frame"><span>TEXT</span></div><div class="product-frame"><span>TEXT</span></div><div class="product-frame"><span>TEXT</span></div><div class="product-frame"><span>TEXT</span></div><div class="product-frame"><span>TEXT</span></div>
      <div class="product-frame"><span>TEXT</span></div><div class="product-frame"><span>TEXT</span></div><div class="product-frame"><span>TEXT</span></div><div class="product-frame"><span>TEXT</span></div><div class="product-frame"><span>TEXT</span></div><div class="product-frame"><span>TEXT</span></div><div class="product-frame"><span>TEXT</span></div><div class="product-frame"><span>TEXT</span></div>
      <div class="product-frame"><span>TEXT</span></div><div class="product-frame"><span>TEXT</span></div><div class="product-frame"><span>TEXT</span></div><div class="product-frame"><span>TEXT</span></div><div class="product-frame"><span>TEXT</span></div><div class="product-frame"><span>TEXT</span></div><div class="product-frame"><span>TEXT</span></div><div class="product-frame"><span>TEXT</span></div>
    </div>

    <div class="product-grid right">
      <div class="product-frame"><span>TEXT</span></div><div class="product-frame"><span>TEXT</span></div><div class="product-frame"><span>TEXT</span></div><div class="product-frame"><span>TEXT</span></div><div class="product-frame"><span>TEXT</span></div><div class="product-frame"><span>TEXT</span></div><div class="product-frame"><span>TEXT</span></div><div class="product-frame"><span>TEXT</span></div>
      <div class="product-frame"><span>TEXT</span></div><div class="product-frame"><span>TEXT</span></div><div class="product-frame"><span>TEXT</span></div><div class="product-frame"><span>TEXT</span></div><div class="product-frame"><span>TEXT</span></div><div class="product-frame"><span>TEXT</span></div><div class="product-frame"><span>TEXT</span></div><div class="product-frame"><span>TEXT</span></div>
      <div class="product-frame"><span>TEXT</span></div><div class="product-frame"><span>TEXT</span></div><div class="product-frame"><span>TEXT</span></div><div class="product-frame"><span>TEXT</span></div><div class="product-frame"><span>TEXT</span></div><div class="product-frame"><span>TEXT</span></div><div class="product-frame"><span>TEXT</span></div><div class="product-frame"><span>TEXT</span></div>
      <div class="product-frame"><span>TEXT</span></div><div class="product-frame"><span>TEXT</span></div><div class="product-frame"><span>TEXT</span></div><div class="product-frame"><span>TEXT</span></div><div class="product-frame"><span>TEXT</span></div><div class="product-frame"><span>TEXT</span></div><div class="product-frame"><span>TEXT</span></div><div class="product-frame"><span>TEXT</span></div>
      <div class="product-frame"><span>TEXT</span></div><div class="product-frame"><span>TEXT</span></div><div class="product-frame"><span>TEXT</span></div><div class="product-frame"><span>TEXT</span></div><div class="product-frame"><span>TEXT</span></div><div class="product-frame"><span>TEXT</span></div><div class="product-frame"><span>TEXT</span></div><div class="product-frame"><span>TEXT</span></div>
      <div class="product-frame"><span>TEXT</span></div><div class="product-frame"><span>TEXT</span></div><div class="product-frame"><span>TEXT</span></div><div class="product-frame"><span>TEXT</span></div><div class="product-frame"><span>TEXT</span></div><div class="product-frame"><span>TEXT</span></div><div class="product-frame"><span>TEXT</span></div><div class="product-frame"><span>TEXT</span></div>
      <div class="product-frame"><span>TEXT</span></div><div class="product-frame"><span>TEXT</span></div><div class="product-frame"><span>TEXT</span></div><div class="product-frame"><span>TEXT</span></div><div class="product-frame"><span>TEXT</span></div><div class="product-frame"><span>TEXT</span></div><div class="product-frame"><span>TEXT</span></div><div class="product-frame"><span>TEXT</span></div>
    </div>

    <p class="note bottom left">Editable text box here</p>
    <p class="note bottom right">Editable text box here</p>
  </div>
</div>
</body>
</html>
```